Modern and appealing business Wordpress site

I've been operating my consulting firm for 5 years and feel like it is time to really improve on my web presence as I'm starting to get more national attention. I had a logo made through this service a couple of years ago, and would like to get a website that matches the look of it. The website will be used to (1) advertise my services (2) provide a brief overview of our management philosophies, and (3) host a resource library database. I understand HTML, but am not as familiar with how to code Wordpress, so I need someone that can help upload themes.

The website can be found at www.trbvexlane.com.

For design, I prefer round designs to square and want the color scheme to match the attached logo. I have included both the full logo and the abbreviated one.

I also have a new picture for CFO uploaded. I plan on getting a new one for the CEO in the coming weeks, so I would like someone that I could get to help make the modification at a later time.

The resource database will be put into a document library (probably Plix4) once the final design is completed rather than having multiple pages with links...just so you know the final vision for the site.

Reach out if you have any questions.

Target Market(s)

Community Action Agencies, Nonprofit Organization Leaders

Industry/Entity Type

Consulting

Coding

Coded - Design and coding required

Font styles to use
Sans Serif

Requirements
Must have
• Must match the color scheme of the attached logo

```html
<!DOCTYPE html>
<html lang="en">
<head>
<meta charset="utf-8">
<title>Tarrow LLC – Leading Organizations to Excellence</title>
<link href="https://fonts.googleapis.com/css2?family=Poppins:wght@400;500;600;700;800&family=Lato:wght@400;700&display=swap" rel="stylesheet">
<style>
:root{
  --blue:#38a3da;
  --blue-deep:#1f7fbd;
  --ink:#111418;
  --text:#4a4f55;
  --white:#ffffff;
  --line:#e4e7ea;
}
*{box-sizing:border-box;margin:0;padding:0}
html,body{width:1200px;height:3839px;overflow:hidden}
body{position:relative;background:var(--white);font-family:'Poppins',sans-serif;color:var(--ink)}
.abs{position:absolute}
a{color:inherit;text-decoration:none}

/* header */
.site-header{position:absolute;left:0;top:0;width:1200px;height:108px;background:var(--white)}
.brand{position:absolute;left:100px;top:28px;display:flex;align-items:center;gap:10px;font-weight:700;font-size:32px;color:var(--blue);letter-spacing:1px}
.brand-dot{width:40px;height:40px;border-radius:50%;background:var(--blue)}
.top-contact{position:absolute;top:24px;left:710px;display:flex;gap:50px;font-size:13px;color:var(--text);align-items:center}
.top-contact span{display:flex;align-items:center;gap:10px}
.main-nav{position:absolute;top:62px;left:404px;display:flex;gap:36px;font-size:15px;font-weight:500}
.main-nav a.active{color:var(--blue);text-decoration:underline}

/* hero */
.hero{position:absolute;left:0;top:108px;width:1200px;height:690px}
.hero-photo{position:absolute;inset:0;background:linear-gradient(100deg,#2d3a44 0%,#5a6b76 45%,#8b98a0 70%,#4b5860 100%)}
.hero-photo::after{content:"";position:absolute;inset:0;background:linear-gradient(90deg,rgba(20,28,36,.55),rgba(20,28,36,.1))}
.hero-copy{position:absolute;left:100px;top:215px;width:520px;color:var(--white)}
.hero-copy h1{font-size:40px;line-height:48px;font-weight:700}
.hero-copy p{margin-top:14px;font-size:14px;line-height:20px;width:500px}
.btn{display:inline-block;font-weight:600;font-size:15px;text-align:center}
.btn-solid{background:var(--blue);color:var(--white)}
.btn-white{background:var(--white);color:var(--ink)}
.hero-copy .btn{margin-top:18px;padding:12px 15px;width:133px}
.dots{position:absolute;left:540px;top:577px;display:flex;gap:6px}
.dots i{display:block;height:5px;width:30px;background:#2c3238;border-radius:3px}
.dots i:first-child{width:62px;background:var(--white)}

/* management */
.section-title{position:absolute;left:0;width:1200px;text-align:center;font-size:34px;font-weight:700}
.msg h2{font-size:24px;font-weight:700}
.msg p{font-size:11.5px;line-height:21px;color:var(--text);margin-top:18px}
.msg blockquote{font-size:13px;font-weight:600;line-height:21px;margin-top:24px}
.msg cite{display:block;font-style:normal;font-weight:700;font-size:17px;line-height:22px;margin-top:18px}
.portrait{position:absolute;border-radius:50%;border:4px solid var(--white);box-shadow:0 6px 20px rgba(0,0,0,.18)}
.role-name{position:absolute;text-align:center;width:400px;font-weight:600;font-size:18px}
.role-title{position:absolute;text-align:center;width:400px;font-weight:700;font-size:20px}

.band{position:absolute;left:0;top:1470px;width:1200px;height:845px}
.on-blue{color:var(--white)}
.on-blue p{color:var(--white)}

/* services */
.service h3{font-size:25px;font-weight:700}
.service p{font-family:'Lato',sans-serif;font-size:14px;line-height:21.5px;color:var(--text);margin-top:18px}
.pill-btn{display:block;margin-top:16px;width:146px;height:44px;line-height:44px;border-radius:22px;background:var(--blue);color:var(--white);font-weight:600;font-size:15px;text-align:center}
.service-photo{position:absolute;width:425px;height:280px;border-radius:140px;box-shadow:0 8px 22px rgba(0,0,0,.15)}
.service-icon{position:absolute;width:60px;height:60px;border-radius:50%;background:var(--white);box-shadow:0 3px 10px rgba(0,0,0,.15);display:flex;align-items:center;justify-content:center}

/* footer */
.site-footer{position:absolute;left:0;top:3490px;width:1200px;height:349px}
.footer-links{position:absolute;left:165px;top:98px;list-style:none;color:var(--white);font-size:14px;line-height:24px}
.footer-rule{position:absolute;top:90px;width:1px;height:190px;background:rgba(255,255,255,.55)}
.footer-brand{position:absolute;left:440px;top:110px;width:320px;display:flex;justify-content:center;align-items:center;gap:12px;color:var(--white);font-weight:700;font-size:44px;letter-spacing:1px}
.footer-brand .brand-dot{width:56px;height:56px;background:var(--white)}
.social{position:absolute;left:526px;top:226px;display:flex;gap:10px}
.social span{width:37px;height:37px;border-radius:50%;background:var(--white)}
.footer-contact{position:absolute;left:830px;top:102px;color:var(--white);font-size:13px;line-height:16px}
.footer-contact div{display:flex;align-items:center;gap:14px;margin-bottom:18px}
.ring{width:34px;height:34px;border-radius:50%;border:1.5px solid var(--white);display:flex;align-items:center;justify-content:center;flex:none}
.copyright{position:absolute;left:0;top:322px;width:1200px;text-align:center;font-size:10px;color:var(--white)}
</style>
</head>
<body>

<header class="site-header">
  <div class="brand"><span class="brand-dot"></span>TARROW LLC</div>
  <div class="top-contact">
    <span><svg width="18" height="18" viewBox="0 0 24 24"><path fill="#38a3da" d="M6.6 10.8a15.1 15.1 0 0 0 6.6 6.6l2.2-2.2c.3-.3.7-.4 1-.2 1.1.4 2.3.6 3.6.6.6 0 1 .4 1 1V20c0 .6-.4 1-1 1A17 17 0 0 1 3 4c0-.6.4-1 1-1h3.5c.6 0 1 .4 1 1 0 1.3.2 2.5.6 3.6.1.3 0 .7-.2 1z"/></svg>(555) 014-2290</span>
    <span style="color:#999">|</span>
    <span><svg width="22" height="16" viewBox="0 0 22 16"><rect x="1" y="1" width="20" height="14" fill="none" stroke="#38a3da" stroke-width="2"/><path d="M1 1l10 8 10-8" fill="none" stroke="#38a3da" stroke-width="2"/></svg>info@tarrowllc.com</span>
  </div>
  <nav class="main-nav">
    <a class="active" href="#">HOME</a><a href="#">ABOUT US</a><a href="#">SERVICES</a><a href="#">OBLT</a><a href="#">PFDL</a><a href="#">RESOURCES</a><a href="#">CONTACT US</a>
  </nav>
</header>

<section class="hero">
  <div class="hero-photo" role="img" aria-label="Photo: a smiling consultant standing at the head of a conference table during a team meeting"></div>
  <div class="hero-copy">
    <h1>LEADING ORGANIZATIONS TO EXCELLENCE!</h1>
    <p>Our approach is not simply based off of theoretical business practices, but on practical solutions to real-life situations learned through more than twenty years of experience.</p>
    <a class="btn btn-solid" href="#">GET STARTED</a>
  </div>
  <div class="dots"><i></i><i></i><i></i></div>
  <svg class="abs" style="left:0;top:600px" width="1200" height="92" viewBox="0 0 1200 92">
    <polygon points="0,62 655,30 655,92 0,92" fill="#38a3da"/>
    <polygon points="0,80 1200,20 1200,92 0,92" fill="#ffffff"/>
  </svg>
</section>

<h2 class="section-title" style="top:806px">OUR MANAGEMENT</h2>

<div class="msg abs" style="left:155px;top:936px;width:455px">
  <h2>CEO'S MESSAGE</h2>
  <p>RT Tarrow, LLC was created to help nonprofits and government contractors meet their basic funding requirements and adopt a Purpose Focused Data Led mindset that promotes positive change in the lives of the people they serve. Our approach is not simply based off of theoretical business practices, but on practical solutions to real-life situations learned through more than twenty years of experience.</p>
  <blockquote>"It was a training, but not your typical training. It leaves you with a new and different take on things. You will find yourself saying 'Wow, I've never thought of it like that before'. You will be left with new and refreshing ideas and different ways to approach</blockquote>
  <cite>– OAKRIDGE COUNTY SENIOR SERVICES</cite>
</div>
<a class="btn btn-solid abs" style="left:166px;top:1273px;width:160px;height:45px;line-height:45px" href="#">READ MORE</a>

<svg class="abs" style="left:615px;top:905px" width="495" height="370" viewBox="0 0 495 370">
  <ellipse cx="260" cy="170" rx="230" ry="140" transform="rotate(-20 260 170)" fill="#eef0f2"/>
  <ellipse cx="120" cy="180" rx="80" ry="120" fill="#dcedf7"/>
</svg>
<div class="portrait" role="img" aria-label="Portrait photo of the CEO in a suit and tie" style="left:678px;top:913px;width:364px;height:364px;background:radial-gradient(circle at 50% 40%,#c9b8a8,#6a5a4e 55%,#232a3a)"></div>
<div class="role-name" style="left:660px;top:1292px;color:var(--blue)">MILES "DEAN" TARROW</div>
<div class="role-title" style="left:660px;top:1324px">OUR CEO</div>

<svg class="band" viewBox="0 0 1200 845" preserveAspectRatio="none">
  <path d="M0 62 Q600 -50 1200 62 L1200 780 Q600 900 0 780 Z" fill="#38a3da"/>
</svg>

<svg class="abs" style="left:120px;top:1560px" width="480" height="380" viewBox="0 0 480 380">
  <ellipse cx="240" cy="190" rx="220" ry="140" transform="rotate(-18 240 190)" fill="#5bb4e2"/>
</svg>
<div class="portrait" role="img" aria-label="Portrait photo of the CFO smiling, with curly hair and glasses" style="left:188px;top:1568px;width:364px;height:364px;background:radial-gradient(circle at 50% 45%,#e3b9a2,#8a5e48 50%,#4b3a30)"></div>
<div class="role-name" style="left:170px;top:1948px;color:#e4f3fb">CLAIRE BENTON TARROW</div>
<div class="role-title abs on-blue" style="left:170px;top:1980px;color:#e4f3fb">OUR CFO</div>

<div class="msg abs on-blue" style="left:620px;top:1590px;width:455px">
  <h2>CFO'S MESSAGE</h2>
  <p>RT Tarrow, LLC was created to help nonprofits and government contractors meet their basic funding requirements and adopt a Purpose Focused Data Led mindset that promotes positive change in the lives of the people they serve. Our approach is not simply based off of theoretical business practices, but on practical solutions to real-life situations learned through more than twenty years of experience.</p>
  <blockquote>"Dean is easy to work with and his expertise allows you to tailor your training to the specific needs of your agency. We highly recommend Dean and his company."</blockquote>
  <cite>-COMMUNITY ACTION PARTNERSHIP OF<br>EAST RIDGEVIEW</cite>
</div>
<a class="btn btn-white abs" style="left:632px;top:1933px;width:160px;height:45px;line-height:45px" href="#">READ MORE</a>

<h2 class="section-title on-blue" style="top:2068px">OUR MISSION</h2>
<p class="abs on-blue" style="left:230px;top:2120px;width:740px;text-align:center;font-size:13px;line-height:21px">To help social service organizations develop a Purpose Focused Data Led mindset that promotes positive change in the lives of the customers they serve.</p>
<a class="btn btn-white abs" style="left:518px;top:2188px;width:165px;height:38px;line-height:38px;font-size:14px" href="#">GET STARTED NOW</a>

<h2 class="section-title" style="top:2395px">OUR SERVICES</h2>

<svg class="abs" style="left:370px;top:2770px" width="400" height="400" viewBox="0 0 400 400">
  <path d="M395 0 V28 H2 V60 M395 340 V308 H2 V280 M395 340 V400" fill="none" stroke="#e4e7ea" stroke-width="2"/>
</svg>

<div class="service abs" style="left:135px;top:2508px;width:420px">
  <h3>TRAINING &amp; CONSULTING</h3>
  <p>We are dedicated to the success of our customers and offer a variety of services focused on improving organizational efficiency and effectiveness through implementation of the Purpose Focused Data Led (PFDL) mindset and the Outcome Based Leadership and Tracking (OBLT) system of organizational management.</p>
  <a class="pill-btn" href="#">READ MORE</a>
</div>
<div class="service-photo" role="img" aria-label="Photo: a team of colleagues meeting around a table with laptops" style="left:638px;top:2492px;background:linear-gradient(120deg,#dfe6ea,#8a9aa4 55%,#4b4e52)"></div>
<div class="service-icon" style="left:606px;top:2594px"><svg width="34" height="34" viewBox="0 0 34 34" fill="none" stroke="#38a3da" stroke-width="1.8"><rect x="3" y="3" width="16" height="11"/><circle cx="11" cy="21" r="3"/><circle cx="24" cy="21" r="3"/><path d="M5 31c0-3 3-5 6-5s6 2 6 5M18 31c0-3 3-5 6-5s6 2 6 5"/></svg></div>

<div class="service-photo" role="img" aria-label="Photo: colleagues reviewing charts on a laptop together" style="left:135px;top:2830px;background:linear-gradient(120deg,#6b7a96,#c9d2e0 50%,#eef1f6)"></div>
<div class="service-icon" style="left:533px;top:2938px"><svg width="34" height="34" viewBox="0 0 34 34" fill="none" stroke="#38a3da" stroke-width="1.8"><rect x="3" y="3" width="16" height="11"/><circle cx="11" cy="21" r="3"/><circle cx="24" cy="21" r="3"/><path d="M5 31c0-3 3-5 6-5s6 2 6 5M18 31c0-3 3-5 6-5s6 2 6 5"/></svg></div>
<div class="service abs" style="left:647px;top:2846px;width:420px">
  <h3>DATA ANALYTICS</h3>
  <p>One the most important, and frequently neglected, areas of organizational management is the analysis of data to accurately identify community needs and track progress towards the successful fulfillment of the entity's purpose. Our goal is to ensure each of our customers is equipped with the tools necessary to obtain objective data that will allow for quality decision making.</p>
  <a class="pill-btn" href="#">READ MORE</a>
</div>

<div class="service abs" style="left:135px;top:3183px;width:420px">
  <h3>STORYTELLING</h3>
  <p>RT Tarrow, LLC is dedicated to ensuring each of our customers is provided with the tools necessary to tell their story through the generation of graphic reports, outreach tools, and videos so they can increase community support and involvement, allowing for a reduced reliance on government funding.</p>
  <a class="pill-btn" style="margin-top:40px" href="#">READ MORE</a>
</div>
<div class="service-photo" role="img" aria-label="Photo: an older presenter gesturing enthusiastically while speaking to a group" style="left:638px;top:3168px;background:linear-gradient(120deg,#3c4a52,#b5926a 50%,#d9b98e)"></div>
<div class="service-icon" style="left:606px;top:3272px"><svg width="34" height="34" viewBox="0 0 34 34" fill="none" stroke="#38a3da" stroke-width="1.8"><rect x="3" y="3" width="16" height="11"/><circle cx="11" cy="21" r="3"/><circle cx="24" cy="21" r="3"/><path d="M5 31c0-3 3-5 6-5s6 2 6 5M18 31c0-3 3-5 6-5s6 2 6 5"/></svg></div>

<footer class="site-footer">
  <svg class="abs" style="left:0;top:0" width="1200" height="349" viewBox="0 0 1200 349" preserveAspectRatio="none">
    <defs><linearGradient id="footerFill" x1="0" y1="0" x2="1" y2="1"><stop offset="0" stop-color="#2a8fcf"/><stop offset="1" stop-color="#1b6fa8"/></linearGradient></defs>
    <path d="M0 70 Q600 -30 1200 70 L1200 349 L0 349 Z" fill="url(#footerFill)"/>
  </svg>
  <ul class="footer-links"><li>HOME</li><li>SERVICES</li><li>OBLT</li><li>PFDL</li><li>RESOURCES</li><li>CONTACT</li></ul>
  <span class="footer-rule" style="left:383px"></span>
  <span class="footer-rule" style="left:778px"></span>
  <div class="footer-brand"><span class="brand-dot"></span>TARROW</div>
  <div class="social" aria-label="Social media links"><span></span><span></span><span></span></div>
  <div class="footer-contact">
    <div><span class="ring"><svg width="14" height="18" viewBox="0 0 14 18"><path d="M7 1a6 6 0 0 0-6 6c0 4.5 6 10 6 10s6-5.5 6-10a6 6 0 0 0-6-6z" fill="none" stroke="#fff" stroke-width="1.6"/><circle cx="7" cy="7" r="2" fill="#fff"/></svg></span><span>418 Larkspur Lane<br>Alden, Georgia 30099</span></div>
    <div><span class="ring"><svg width="16" height="12" viewBox="0 0 16 12"><rect x="1" y="1" width="14" height="10" fill="none" stroke="#fff" stroke-width="1.4"/><path d="M1 1l7 6 7-6" fill="none" stroke="#fff" stroke-width="1.4"/></svg></span><span>info@tarrowllc.com</span></div>
    <div><span class="ring"><svg width="14" height="14" viewBox="0 0 24 24"><path fill="#fff" d="M6.6 10.8a15.1 15.1 0 0 0 6.6 6.6l2.2-2.2c.3-.3.7-.4 1-.2 1.1.4 2.3.6 3.6.6.6 0 1 .4 1 1V20c0 .6-.4 1-1 1A17 17 0 0 1 3 4c0-.6.4-1 1-1h3.5c.6 0 1 .4 1 1 0 1.3.2 2.5.6 3.6.1.3 0 .7-.2 1z"/></svg></span><span>(555) 014-2290</span></div>
  </div>
  <p class="copyright">Copyright © 2022 Tarrow LLC . All Rights Reserved</p>
</footer>

</body>
</html>
```